Business Cards/Stationary for New Travel Agency
Bright Compass Travel
Business Cards/Stationary for New Travel Agency - Travel
Creative Brief
Professional
Melvor Tansley
Leisure and Business Travel Agent
OakVale Court Office, 418 Brindle Blvd., 4th Floor, Santa Monica, CA, 90408 Tel: 310-555-0193 Go Yonder Office, 526 Fenwick Ave., #C, Santa Monica, CA, 90406 Tel: 310-555-0147 ext. 3871
melvor@brightcompasstravelagency.example
www.brightcompasstravelagency.example
Go Yonder Affiliate - CST# 2937516-82
Contact information for both addresses needed on front of business cards. (Two separate columns with each address may look better.) Font size should be big as possible without looking too crowded. Affiliate/License No. can be in small print on bottom of business cards.
Logo on white background. (Big)
drumreed drumreed
loverdan loverdan
#80 - On the back, can you please change Go Yonder Affiliate to Cobble Tours Affiliate and make the font size bigger? Can you please make the font size bigger for the front of the card? (When I adjust the card on the screen to actual size, the font size is too small which will make it difficult for older people to read.)
To all designers: Please upload business card design in mock-up/printer-ready format to see actual size and text. Thank you!!

```html
<!DOCTYPE html>
<html lang="en">
<head>
<meta charset="utf-8">
<title>Bright Compass Travel – Business Card</title>
<link href="https://fonts.googleapis.com/css2?family=PT+Serif:wght@400;700&display=swap" rel="stylesheet">
<style>
  :root {
    --stage: #ececec;
    --paper: #ffffff;
    --navy: #1d4f91;
    --deep-navy: #1f4670;
    --teal: #2a8db3;
    --gold: #f0b21a;
    --green: #3b8a2f;
    --ink: #1d4f91;
    --label: #222222;
  }
  html, body {
    margin: 0;
    padding: 0;
    width: 1200px;
    height: 778px;
    overflow: hidden;
    background: var(--stage);
    font-family: "PT Serif", Georgia, serif;
  }
  .canvas { position: relative; width: 1200px; height: 778px; }

  .side-label {
    position: absolute;
    font-size: 20px;
    font-style: italic;
    font-weight: 700;
    color: var(--label);
  }
  .side-label--front { left: 40px; top: 60px; }
  .side-label--back { left: 540px; top: 692px; }

  .brand-display {
    position: absolute;
    right: 60px;
    top: 70px;
    display: flex;
    align-items: center;
    gap: 12px;
    font-size: 30px;
    font-weight: 700;
    color: var(--navy);
    letter-spacing: 1px;
  }
  .brand-mark-dot { width: 18px; height: 18px; border-radius: 50%; background: var(--gold); flex: none; }

  .card {
    position: absolute;
    width: 560px;
    height: 320px;
    overflow: hidden;
    box-shadow: 0 6px 18px rgba(0,0,0,0.22);
  }
  .card--front { left: 40px; top: 100px; background: var(--paper); }
  .card--back { left: 600px; top: 360px; background: var(--deep-navy); }

  .front-brand {
    position: absolute;
    right: 24px;
    top: 34px;
    display: flex;
    align-items: center;
    gap: 8px;
    font-size: 21px;
    font-weight: 700;
    color: var(--navy);
  }
  .front-brand .brand-mark-dot { width: 12px; height: 12px; }

  .agent { position: absolute; left: 22px; top: 72px; color: var(--ink); }
  .agent-name { font-size: 22px; margin: 0; font-weight: 400; }
  .agent-title { font-size: 12px; margin: 2px 0 0; }

  .office { position: absolute; color: var(--ink); font-size: 12.5px; font-style: normal; line-height: 1.35; }
  .office--primary { left: 22px; top: 132px; }
  .office--secondary { left: 262px; top: 132px; }
  .office p { margin: 0; }

  .contact-list { position: absolute; list-style: none; margin: 0; padding: 0; color: var(--ink); font-size: 13.5px; }
  .contact-list li { display: flex; align-items: center; gap: 6px; margin-bottom: 3px; white-space: nowrap; }
  .contact-list--primary { left: 22px; top: 226px; }
  .contact-list--secondary { left: 262px; top: 208px; font-size: 12.5px; }
  .icon { width: 13px; height: 13px; flex: none; }

  .web { position: absolute; left: 22px; top: 284px; font-size: 14px; color: var(--green); }

  .stripe { position: absolute; left: 0; bottom: 0; width: 100%; height: 5px; display: flex; }
  .stripe span { height: 100%; }
  .stripe-gold { flex: 2.2; background: var(--gold); }
  .stripe-navy { flex: 1.4; background: var(--navy); }
  .stripe-teal { flex: 2.4; background: var(--teal); }

  .back-brand {
    position: absolute;
    right: 36px;
    top: 135px;
    display: flex;
    align-items: center;
    gap: 10px;
    font-size: 26px;
    font-weight: 700;
    color: #ffffff;
  }
  .back-brand .brand-mark-dot { width: 14px; height: 14px; background: rgba(255,255,255,0.85); }
  .affiliate {
    position: absolute;
    left: 360px;
    top: 268px;
    font-size: 10px;
    line-height: 1.4;
    color: var(--gold);
  }
  .affiliate p { margin: 0; }
</style>
</head>
<body>
<main class="canvas">
  <span class="side-label side-label--front">Front</span>
  <span class="side-label side-label--back">Back</span>

  <div class="brand-display"><span class="brand-mark-dot"></span>Bright Compass Travel</div>

  <section class="card card--front">
    <div class="front-brand"><span class="brand-mark-dot"></span>Bright Compass Travel</div>

    <div class="agent">
      <h1 class="agent-name">Melvor Tansley</h1>
      <p class="agent-title">Leisure And Business Travel Agent</p>
    </div>

    <address class="office office--primary">
      <p>OakVale Court Office,</p>
      <p>418 Brindle Blvd., 4th Floor,</p>
      <p>Santa Monica, Ca, 90408</p>
      <p>Tel: 310-555-0193</p>
    </address>

    <address class="office office--secondary">
      <p>Go Yonder Office,</p>
      <p>526 Fenwick Ave., #C,</p>
      <p>Santa Monica, Ca, 90406</p>
      <p>Tel: 310-555-0147 ext. 3871</p>
    </address>

    <ul class="contact-list contact-list--primary">
      <li>
        <svg class="icon" viewBox="0 0 14 14"><path d="M3 1h3l1 3-2 1.2a7 7 0 0 0 3.8 3.8L10 7l3 1v3a2 2 0 0 1-2 2C5.5 13 1 8.5 1 3a2 2 0 0 1 2-2z" fill="var(--gold)"/></svg>
        800-555-0126
      </li>
      <li>
        <svg class="icon" viewBox="0 0 14 14"><rect x="4" y="1" width="6" height="12" rx="1.2" fill="var(--gold)"/><rect x="5" y="2.5" width="4" height="7" fill="#fff"/></svg>
        310-555-0178
      </li>
    </ul>

    <ul class="contact-list contact-list--secondary">
      <li>
        <svg class="icon" viewBox="0 0 14 14"><rect x="1" y="5" width="12" height="7" rx="1" fill="var(--gold)"/><rect x="3" y="2" width="8" height="4" fill="var(--gold)"/><rect x="4" y="7" width="6" height="3" fill="#fff"/></svg>
        310-555-0162
      </li>
      <li>
        <svg class="icon" viewBox="0 0 14 14"><rect x="1" y="3" width="12" height="8" rx="1" fill="var(--gold)"/><path d="M1.5 3.5 7 8l5.5-4.5" fill="none" stroke="#fff" stroke-width="1.2"/></svg>
        melvor@brightcompasstravelagency.example
      </li>
    </ul>

    <a class="web">www.brightcompasstravelagency.example</a>

    <div class="stripe"><span class="stripe-gold"></span><span class="stripe-navy"></span><span class="stripe-teal"></span></div>
  </section>

  <section class="card card--back">
    <div class="back-brand"><span class="brand-mark-dot"></span>Bright Compass Travel</div>
    <div class="affiliate">
      <p>Go Yonder Affiliate</p>
      <p>CST# 2937516-82</p>
    </div>
  </section>
</main>
</body>
</html>
```